Brightwater Confections needs to spice up their website with a new look and feel.

Brightwater Confections needs to update it's web site design, look and feel. We are a family run company that enhances personal well-being through delicious products like gourmet chocolate with harmonic process (the science that is behind our product). We are looking to create an intentional web space with a bit of humor.

Well-being is the first and foremost message we want to promote. This is the feeling we want the consumers to receive when they enter the site. The consumer needs to learn how they can enhance their well-being with our product with education but also with a bit of humor. We want it light but not making fun of like a "Sunny Days Co" website.

Splash Page goals:
Clear and simple. Not too much copy or images.
Promote well-being immediately with visuals and the front page content
Humorous
Love of Life

Web sites we like:
Www.wearethekindfolk.com
www.sunnydaysco.com
www.nourishworks.com

Target Market(s)

25-65 year olds upper middle class skews female

Industry/Entity Type

Education

Requirements
Must have
• Our "tiny fellow logo" (can be played with a bit but must remain the "dude")

Splash Page Tabs: (numbers represent the tab, the dashes mean they are part of the drop down menu of the tabs)

1.Intention
-Why do you need Intention?
-Intentional Give-back
-Intentional Causes
-Donate now
-Harmonic Process
-Step toward joy 1 min clip
-Scientific Research
2. Shop
-Indulgent Line
-Healthy Line
-RX program ( more on this on slide #10)
Full online site
4. Chocolate Tasting Meditation (we will provide tunebox link)
3. About
4. Contact
5. Blog (www.brightwaterconfections-blog.com)
6. Press

Copy that is similar to the one already on our site (www.brightwaterconfections.com) or the power point attached about our company

Nice to have
• A place for a video to play on the front page (attached file) - Step toward joy (video uploaded in the power point presentation

```html
<!DOCTYPE html>
<html lang="en">
<head>
<meta charset="utf-8">
<title>Brightwater Confections – Offering</title>
<link rel="stylesheet" href="https://fonts.googleapis.com/css2?family=Arimo:wght@400;700&display=swap">
<style>
:root{
  --page-bg:#ffffff;
  --brand-brown:#4a2412;
  --brand-orange:#e0892a;
  --rule-orange:#e08a2c;
  --nav-text:#3a3a3a;
  --body-text:#1a1a1a;
  --hero-top:#f3a032;
  --hero-mid:#e27414;
  --hero-low:#b8460a;
  --hero-bottom:#3a1406;
  --badge-dark:#1c1c1c;
}
*{margin:0;padding:0;box-sizing:border-box}
html,body{width:1200px;height:1000px;overflow:hidden;background:var(--page-bg)}
body{font-family:"Arimo",Arial,sans-serif;color:var(--body-text);position:relative}

.site-header{position:absolute;left:0;top:0;width:1200px;height:170px;display:flex;flex-direction:column;align-items:center}
.brand-mark{margin-top:58px;width:48px;height:48px;border-radius:50%;background:var(--brand-orange)}
.brand-name{margin-top:17px;font-size:15px;font-weight:700;letter-spacing:.5px;color:var(--brand-brown);text-transform:uppercase}

.header-rule{position:absolute;left:171px;top:169px;width:854px;height:3px;background:var(--rule-orange)}

.main-nav{position:absolute;left:171px;top:189px;width:854px;display:flex;justify-content:space-between;padding:0 12px 0 16px}
.main-nav a{font-size:14.5px;font-weight:700;color:var(--nav-text);text-decoration:none}

.hero{position:absolute;left:171px;top:219px;width:854px;height:472px;overflow:hidden;
  background:linear-gradient(180deg,var(--hero-top) 0%,var(--hero-mid) 40%,var(--hero-low) 75%,var(--hero-bottom) 100%)}
.hero-title{position:absolute;right:18px;top:42px;font-size:28px;font-weight:700;color:var(--brand-brown);letter-spacing:.3px}
.hero-tagline{position:absolute;right:18px;top:73px;font-size:16.5px;color:var(--brand-brown)}

.content{position:absolute;left:172px;top:716px;width:856px}
.content h2{font-size:19px;font-weight:700;margin-bottom:16px}
.content p{font-size:11.3px;line-height:15px;margin-bottom:15px;letter-spacing:-.15px}
.content h3{font-size:15px;font-weight:700;margin-top:18px}
.causes{margin-top:36px}
.causes p{width:720px}

.partner-badge{position:absolute;left:925px;top:906px;width:100px;height:100px;border-radius:50%;background:var(--badge-dark)}
</style>
</head>
<body>
<header class="site-header">
  <div class="brand-mark" aria-hidden="true"></div>
  <div class="brand-name">Brightwater Confections</div>
</header>
<div class="header-rule"></div>

<nav class="main-nav">
  <a href="#">Home</a>
  <a href="#">Intention</a>
  <a href="#">Shop</a>
  <a href="#">Tasting Meditation</a>
  <a href="#">About</a>
  <a href="#">Contact</a>
  <a href="#">Blog</a>
  <a href="#">Press</a>
</nav>

<section class="hero" role="img" aria-label="Photograph of a woman in a yoga tree pose silhouetted on a hilltop against an orange sunset sky">
  <div class="hero-title">GOURMET CHOCOLATE</div>
  <div class="hero-tagline">Embedded with positive intention for energy, vigor and well-being.</div>
</section>

<main class="content">
  <section class="offering">
    <h2>Offering</h2>
    <p>Our core mission at Brightwater Confections is to do no harm and benefit others through intentional living. We hope that our offering of intentional products inspires those who are open to the possibility of living an intentional life. This begins with simple gestures. It is in the offering of such gestures that the joy of life resides. That is why we offer this chocolate, our best effort and the embodiment of our desire to live an intentional life.</p>
    <p>We endeavor to stay true to our mission every day, by taking one step at a time. We support continued scientific research in the field of intentional life and at the same time support individuals who are demonstrating the power of living intentionally through their community-building efforts and by planning events for the benefit of others.</p>
  </section>
  <section class="causes">
    <h2>Intentional Causes</h2>
    <p>Brightwater Confections believes in living life intentionally by giving back to intentional causes. We donate 10% of our proceeds to intentional causes, including the following</p>
    <h3>Tidewater Foundation</h3>
  </section>
</main>

<div class="partner-badge" aria-hidden="true"></div>
</body>
</html>
```